Rack Card Design for an Ayurvedic Beauty Product Project

Hello, I need to have rack cards. The rack cards would be about 3 products we are showcasing at an event. I am a cosmetic company. I have a logo and basic design ideas. I have attached some product images and info. By no means am I a designer so please excuse my messy AI files. Please feel free to design this as feminine as you like. :)

Target Market(s)

Beauty industry, organic, holistic, ayurveda

Industry/Entity Type

Cosmetic

```html
<!DOCTYPE html>
<html lang="en">
<head>
<meta charset="utf-8">
<title>Velvet Lotus Rack Card</title>
<link href="https://fonts.googleapis.com/css2?family=Questrial&family=Open+Sans:wght@400;600;700&display=swap" rel="stylesheet">
<style>
  :root {
    --plum: #8b2f6f;
    --plum-deep: #6e2358;
    --plum-light: #a2448a;
    --gold: #b99b6b;
    --gold-deep: #9c7f52;
    --gold-light: #d6bf93;
    --ink: #5b5b5b;
    --paper: #ffffff;
    --mist: #f4f1f3;
  }
  * { margin: 0; padding: 0; box-sizing: border-box; }
  html, body { width: 1200px; height: 2607px; overflow: hidden; background: var(--paper); }
  .rack-card { position: relative; width: 1200px; height: 2607px; overflow: hidden; background: var(--paper); font-family: "Open Sans", sans-serif; }

  .hero-photo {
    position: absolute; left: 510px; top: 0; width: 690px; height: 716px;
    background: linear-gradient(120deg, #f3ece8 0%, #e9d8cf 45%, #d9bfb1 70%, #f1ebe8 100%);
  }
  .brand { position: absolute; left: 128px; top: 240px; display: flex; align-items: center; gap: 18px; }
  .brand-dot { width: 34px; height: 34px; border-radius: 50%; background: var(--gold); }
  .brand-name { font-family: "Questrial", sans-serif; font-size: 40px; color: var(--gold); letter-spacing: 2px; }

  .headline {
    position: absolute; left: 128px; top: 455px;
    font-family: "Questrial", sans-serif; font-size: 66px; line-height: 70px; color: var(--plum-light);
  }
  .headline strong { font-family: "Open Sans", sans-serif; font-weight: 700; color: var(--gold); }

  .intro-band {
    position: absolute; left: 0; top: 716px; width: 1200px; height: 537px;
    background: linear-gradient(90deg, var(--plum-deep), var(--plum) 50%, var(--plum-light));
    padding: 70px 100px 0;
  }
  .intro-text { color: var(--paper); font-size: 33px; line-height: 52px; text-align: justify; }

  .ribbon {
    position: absolute; height: 108px; display: flex; flex-direction: column; justify-content: center;
    color: var(--paper); font-weight: 700; font-size: 38px; line-height: 42px; text-transform: uppercase;
  }
  .ribbon--gold { background: linear-gradient(90deg, var(--gold-deep), var(--gold) 60%, var(--gold-light)); border-radius: 0 54px 54px 0; padding-left: 27px; }
  .ribbon--plum { background: linear-gradient(90deg, var(--plum-deep), var(--plum)); border-radius: 54px 0 0 54px; padding-left: 38px; }

  .product-copy { position: absolute; font-size: 38px; line-height: 49px; color: var(--ink); }

  .product-shot { position: absolute; }
  .tube { background: linear-gradient(90deg, var(--plum-deep), var(--plum-light) 50%, var(--plum-deep)); border-radius: 10px 10px 4px 4px; }
  .tube-cap { position: absolute; left: 0; bottom: -60px; width: 100%; height: 60px; background: linear-gradient(90deg, var(--gold-deep), var(--gold-light), var(--gold-deep)); border-radius: 0 0 8px 8px; }
  .jar { background: linear-gradient(90deg, #e9e7e5, #ffffff 50%, #dcd9d6); border-radius: 12px; }
  .jar-lid { position: absolute; left: 0; top: 0; width: 100%; height: 55px; background: linear-gradient(90deg, var(--gold-deep), var(--gold-light), var(--gold-deep)); border-radius: 12px 12px 4px 4px; }

  .call-band {
    position: absolute; left: 0; top: 2481px; width: 1200px; height: 126px;
    background: linear-gradient(90deg, var(--plum-deep), var(--plum));
    display: flex; align-items: center; justify-content: center;
    font-family: "Questrial", sans-serif; font-size: 62px; color: var(--paper); letter-spacing: 1px;
  }
</style>
</head>
<body>
<main class="rack-card">
  <div class="hero-photo" role="img" aria-label="Photograph of a woman's torso in a white bra, arms crossed"></div>

  <div class="brand">
    <span class="brand-dot"></span>
    <span class="brand-name">VELVET LOTUS</span>
  </div>

  <h1 class="headline">Enhance<br>the <strong>beauty</strong> of<br>your <strong>Breast</strong></h1>

  <section class="intro-band">
    <p class="intro-text">Velvet Lotus curates organic infused products where holistic skin care meets a luxurious experience. Each ingredient is carefully selected; providing Ayurvedic herbs, rich minerals &amp; elements. Stimulating hydration and anti-oxidants to lift, firm and illuminate your skin. We believe in connecting with your inner mantra, stimulating higher vibrations, self-esteem, positive mind and soul. As a brand we work with our experts/suppliers of Ayurveda to ensure that our products meet the quality, wholesome healing that you need.</p>
  </section>

  <div class="ribbon ribbon--gold" style="left:77px; top:1317px; width:703px;">
    <span>Velvet Lotus Firming and</span><span>Lifting Breast Toner</span>
  </div>
  <div class="product-shot" style="left:900px; top:1317px; width:150px; height:230px;" role="img" aria-label="Purple toner tube with gold cap">
    <div class="tube" style="width:100%; height:100%;"></div>
    <div class="tube-cap"></div>
  </div>
  <p class="product-copy" style="left:104px; top:1440px; width:760px;">Using all natural Ayurvedic herbs, our breast toner, prepares the area for maximum absorption, giving you the best results and the most invigorating treatment</p>

  <div class="product-shot" style="left:115px; top:1700px; width:255px; height:245px;" role="img" aria-label="White cream jar with gold lid and purple label">
    <div class="jar" style="width:100%; height:100%;"></div>
    <div class="jar-lid"></div>
  </div>
  <div class="ribbon ribbon--plum" style="left:410px; top:1693px; width:715px;">
    <span>Velvet Lotus Firming and</span><span>Lifting Breast Cream</span>
  </div>
  <p class="product-copy" style="left:448px; top:1830px; width:680px;">Using all natural Ayurvedic herbs, our breast cream helps enhance, tighten, and lift your breast</p>

  <div class="ribbon ribbon--gold" style="left:77px; top:2033px; width:703px;">
    <span>Velvet Lotus Firming and</span><span>Toning Breast Serum</span>
  </div>
  <div class="product-shot" style="left:925px; top:2033px; width:125px; height:330px;" role="img" aria-label="Slim purple serum tube with gold cap">
    <div class="tube" style="width:100%; height:100%;"></div>
    <div class="tube-cap"></div>
  </div>
  <p class="product-copy" style="left:104px; top:2170px; width:760px;">Using all natural Ayurvedic herbs, and a touch of 24k gold, our serum enhances the experience and quality of results when partnered with the Velvet Lotus Firming and Lifting Breast Cream providing an all-dayboosting experience</p>

  <footer class="call-band">CALL US 555 010 2040</footer>
</main>
</body>
</html>
```